Bottle Label for Premium Gold CBD Oil

10 ml CBD-Oil bottle. The job is pretty straight forward and everything you need is prepared. However, the design part of the creative part ^^ The design of a lot of follow-up products we could do together. We thought about an exclusive / minimalist approach to Morvo. The bottle itself is delivered in a drawer box which looks much better than the cheap packages of the competition. Everything about the product is supposed to be honest and of high quality. The product is even more cost-effective than CBD-Oils. Key feature of the product is its deeply golden color. The design should be in harmony with this color. The customer pays a high price for this little bottle and has high expectations. Accordingly, the label should express itself and the product is worth every cent. Which it is by the way. If you would like to see the labels of the competition, just type in "CBD OIL" on "warenzelt.de". However, we are currently the only ones with a new filtration and the corresponding golden color. This label is going to be the base of a whole series of products. If we are happy with your label design, we will do a lot of following up designs with you. The logo design is already done and just needs to be implemented. We are looking forward to your designs. Many, many thanks in advance
Target Market(s)
Customers who want to use the absolute top CBD product on the market in order to improve their health
Colors
Designer to choose colors to be used in the design.
Requirements
Must have
- Please read the pdf-file with detailed descriptions and pictures. The costomer should always see that our product is of the highest quality. Please feel free to stick to our suggestions / ideas since I we are no designers. If you have your own cool approach, just submit it ^^
Nice to have
- We think it would be nice to have a drop out on the front of the label. We could imagine an exclusive / minimalist approach similar to Morvo

```html
<!DOCTYPE html>
<html lang="de">
<head>
<meta charset="utf-8">
<title>CBD-Hanföl Premium Gold – Etiketten</title>
<link rel="stylesheet" href="https://fonts.googleapis.com/css2?family=Oswald:wght@600&family=Montserrat:wght@400;500&family=Roboto+Condensed:wght@400&display=swap">
<style>
  :root {
    --canvas-top: #e9e9e9;
    --canvas-bottom: #f7f7f7;
    --label-dark: #2a2220;
    --label-light: #ffffff;
    --ink-dark: #1c1a1a;
    --ink-light: #ffffff;
    --label-shadow: rgba(0, 0, 0, 0.18);
  }

  * { box-sizing: border-box; margin: 0; padding: 0; }

  html, body {
    width: 1200px;
    height: 800px;
    overflow: hidden;
  }

  body {
    background: linear-gradient(180deg, var(--canvas-top), var(--canvas-bottom));
    display: flex;
    align-items: center;
    justify-content: center;
    gap: 110px;
  }

  .label {
    position: relative;
    width: 340px;
    height: 492px;
    display: flex;
    flex-direction: column;
    align-items: center;
    box-shadow: 0 10px 30px var(--label-shadow);
    color: var(--ink);
  }

  .label--dark { background: var(--label-dark); --ink: var(--ink-light); }
  .label--light { background: var(--label-light); --ink: var(--ink-dark); }

  .label__arc {
    display: block;
    width: 280px;
    height: 120px;
    margin-top: 40px;
  }

  .label__arc-text {
    font-family: "Montserrat", sans-serif;
    font-weight: 400;
    font-size: 17px;
    letter-spacing: 6px;
    fill: var(--ink);
  }

  .label__arc-mark { fill: none; stroke: var(--ink); stroke-width: 1.5; }

  .label__brand {
    margin-top: -18px;
    font-family: "Montserrat", sans-serif;
    font-weight: 400;
    font-size: 13px;
    letter-spacing: 1.5px;
    line-height: 1.3;
    text-transform: uppercase;
    text-align: center;
  }

  .label__title {
    margin-top: 18px;
    font-family: "Oswald", sans-serif;
    font-weight: 600;
    font-size: 50px;
    line-height: 1;
    letter-spacing: 0.5px;
  }

  .label__drop {
    display: block;
    width: 36px;
    height: 52px;
    margin-top: 16px;
  }

  .label__drop path { fill: none; stroke: var(--ink); stroke-width: 2.4; }

  .label__strength {
    margin-top: 12px;
    font-family: "Montserrat", sans-serif;
    font-weight: 500;
    font-size: 19px;
    letter-spacing: 1px;
  }

  .label__grade {
    margin-top: 18px;
    font-family: "Montserrat", sans-serif;
    font-weight: 500;
    font-size: 23px;
    letter-spacing: 5px;
  }

  .label__rule {
    width: 320px;
    height: 2px;
    margin-top: 10px;
    background: var(--ink);
  }

  .label__specs {
    margin-top: 10px;
    font-family: "Roboto Condensed", sans-serif;
    font-weight: 400;
    font-size: 19px;
    white-space: nowrap;
  }
</style>
</head>
<body>

  <article class="label label--dark">
    <svg class="label__arc" viewBox="0 0 280 120" aria-hidden="true">
      <defs>
        <path id="arc-dark" d="M 22 118 A 118 104 0 0 1 258 118"/>
      </defs>
      <text class="label__arc-text"><textPath href="#arc-dark" startOffset="50%" text-anchor="middle">VOLLSPEKTUM</textPath></text>
      <circle class="label__arc-mark" cx="140" cy="84" r="14"/>
    </svg>
    <p class="label__brand">Goldtal<br>Hanfwerk</p>
    <h1 class="label__title">CBD-HANFÖL</h1>
    <svg class="label__drop" viewBox="0 0 36 52" aria-hidden="true">
      <path d="M18 3 C 12 14, 4 24, 4 33 A 14 14 0 0 0 32 33 C 32 24, 24 14, 18 3 Z"/>
    </svg>
    <p class="label__strength">10 %</p>
    <p class="label__grade">PREMIUM GOLD</p>
    <div class="label__rule"></div>
    <p class="label__specs">10 ml | 250 Tropfen | 1000 mg CBD</p>
  </article>

  <article class="label label--light">
    <svg class="label__arc" viewBox="0 0 280 120" aria-hidden="true">
      <defs>
        <path id="arc-light" d="M 22 118 A 118 104 0 0 1 258 118"/>
      </defs>
      <text class="label__arc-text"><textPath href="#arc-light" startOffset="50%" text-anchor="middle">VOLLSPEKTUM</textPath></text>
      <circle class="label__arc-mark" cx="140" cy="84" r="14"/>
    </svg>
    <p class="label__brand">Goldtal<br>Hanfwerk</p>
    <h1 class="label__title">CBD-HANFÖL</h1>
    <svg class="label__drop" viewBox="0 0 36 52" aria-hidden="true">
      <path d="M18 3 C 12 14, 4 24, 4 33 A 14 14 0 0 0 32 33 C 32 24, 24 14, 18 3 Z"/>
    </svg>
    <p class="label__strength">10 %</p>
    <p class="label__grade">PREMIUM GOLD</p>
    <div class="label__rule"></div>
    <p class="label__specs">10 ml | 250 Tropfen | 1000 mg CBD</p>
  </article>

</body>
</html>
```